Email Banner Ad for Tidewell Energy company

We are looking for an Email Banner Ad for all emails which is link to website

Regarding MEES compliance coming in April 2018

All the details can be found on our website www.lumenvista.co.uk

Our current footer is attached from last year and we are looking for a new one

Target Market(s)

Property companies and investor

Industry/Entity Type

It Company

Requirements
Must have
• a link to website
• must be the size to go at the bottom of emails
Nice to have
• similar to website
• similar to the advertisement we have had done already

```html
<!DOCTYPE html>
<html lang="en">
<head>
<meta charset="utf-8">
<title>Tidewell Energy – Email Banner</title>
<link rel="stylesheet" href="https://fonts.googleapis.com/css2?family=Roboto:wght@400;500&display=swap">
<style>
  :root {
    --canvas-bg: #b7b7b7;
    --green-deep: #0f6a46;
    --green-mid: #117148;
    --green-bright: #2ba64a;
    --accent-orange: #e8603c;
    --text-white: #ffffff;
    --frame: #2a2a2a;
    --city-light: #e9ecec;
    --city-mid: #8d9393;
    --city-dark: #3c4242;
  }
  html, body {
    margin: 0;
    padding: 0;
    width: 1200px;
    height: 1200px;
    overflow: hidden;
    background: var(--canvas-bg);
  }
  .email-banner {
    position: absolute;
    left: 182px;
    top: 551px;
    width: 910px;
    height: 112px;
    box-sizing: border-box;
    border: 1px solid var(--frame);
    background: linear-gradient(90deg, var(--green-deep) 0%, var(--green-mid) 35%, var(--green-bright) 68%, var(--green-bright) 100%);
    overflow: hidden;
    font-family: "Roboto", Arial, sans-serif;
    color: var(--text-white);
  }
  .brand {
    position: absolute;
    left: 38px;
    top: 38px;
    display: flex;
    align-items: center;
    gap: 6px;
    font-size: 26px;
    font-weight: 500;
    line-height: 1;
    letter-spacing: 0.2px;
  }
  .brand-mark {
    width: 8px;
    height: 8px;
    background: var(--accent-orange);
  }
  .divider {
    position: absolute;
    left: 145px;
    top: 24px;
    width: 1px;
    height: 66px;
    background: var(--text-white);
    opacity: 0.85;
  }
  .headline {
    position: absolute;
    left: 163px;
    top: 30px;
    margin: 0;
    font-size: 21px;
    font-weight: 400;
    line-height: 30px;
  }
  .headline .date {
    color: var(--accent-orange);
  }
  .city-visual {
    position: absolute;
    top: 0;
    right: 0;
    width: 340px;
    height: 110px;
  }
</style>
</head>
<body>
  <a class="email-banner" href="https://www.lumenvista.co.uk" aria-label="Tidewell Energy – Minimum Energy Performance Standards, www.lumenvista.co.uk">
    <div class="brand"><span class="brand-name">Tidewell</span><span class="brand-mark"></span></div>
    <div class="divider"></div>
    <p class="headline">Minimum Energy Performance Standards<br>(MEPS) England, <span class="date">April&nbsp; 2018</span></p>
    <svg class="city-visual" viewBox="0 0 340 110" preserveAspectRatio="none">
      <defs>
        <linearGradient id="cityTone" x1="0" y1="0" x2="1" y2="0">
          <stop offset="0" stop-color="var(--city-dark)"/>
          <stop offset="0.35" stop-color="var(--city-mid)"/>
          <stop offset="0.6" stop-color="var(--city-light)"/>
          <stop offset="1" stop-color="var(--city-mid)"/>
        </linearGradient>
      </defs>
      <polygon class="accent-stripe" points="25,0 31,0 10,110 -3,110" fill="var(--accent-orange)"/>
      <polygon points="31,0 34,0 13,110 10,110" fill="#ffffff"/>
      <polygon class="city-photo" points="34,0 340,0 340,110 13,110" fill="url(#cityTone)" role="img" aria-label="Photograph of city office towers and historic buildings"/>
    </svg>
  </a>
</body>
</html>
```